Healthcare marketing Website design

This is for a healthcare marketing agency
All details and brief included in the files

I need the design to be incredible!

5 pages to be designed
Home page
About
Portfolio Page
Services
Start your project page

If you need more stock images - download preview images from kelmora pix so I can purchase at a later date

```html
<!DOCTYPE html>
<html lang="en">
<head>
<meta charset="utf-8">
<title>Halcyon Consulting — Healthcare Marketing</title>
<link href="https://fonts.googleapis.com/css2?family=Urbanist:wght@400;500;600;700&display=swap" rel="stylesheet">
<style>
:root{
  --navy:#1f3157;
  --navy-deep:#131d36;
  --navy-card:#3b4b73;
  --panel:#26396a;
  --accent:#1ba6e4;
  --btn:#1896d3;
  --white:#ffffff;
  --muted:#c9d3e6;
  --line:#8fa0c4;
}
*{box-sizing:border-box;margin:0;padding:0}
html,body{width:1200px;height:4501px;overflow:hidden}
body{position:relative;font-family:"Urbanist",sans-serif;color:var(--white);
  background:linear-gradient(180deg,#2a3b66 0,#22335e 600px,#1f3157 1500px,#223561 2500px,#1a2848 2620px,var(--navy-deep) 2800px,#182544 3300px,#22345f 3600px,#22345f 4030px,var(--navy-deep) 4030px,var(--navy-deep) 4501px)}
.abs{position:absolute}
.accent{color:var(--accent)}
.center{left:0;width:1200px;text-align:center}
.btn{position:absolute;display:flex;align-items:center;justify-content:center;font-size:11px;font-weight:700;border-radius:3px}
.btn-primary{background:var(--btn);color:var(--white)}
.btn-light{background:var(--white);color:#1f3157}

/* header */
.hero-photo{left:0;top:0;width:1200px;height:640px;
  background:linear-gradient(180deg,rgba(160,170,190,.85) 0,rgba(110,120,150,.8) 220px,rgba(60,75,115,.85) 420px,#2a3b66 620px)}
.brand{left:101px;top:22px;display:flex;align-items:center;gap:8px;font-size:28px;line-height:32px;font-weight:500;color:var(--white)}
.brand-dot{width:22px;height:22px;border-radius:50%;background:var(--accent)}
.brand-sub{left:131px;top:56px;font-size:7px;letter-spacing:.5px;color:var(--white)}
.nav{top:36px;left:656px;display:flex;gap:30px;font-size:12px;font-weight:500}
.follow{top:9px;left:994px;font-size:11px;display:flex;align-items:center;gap:8px}
.soc{width:8px;height:8px;border-radius:50%;border:1.5px solid var(--white);display:inline-block}
.hero-kicker{top:330px;font-size:14px;line-height:17px}
.hero-title{top:370px;font-size:36px;font-weight:700;line-height:46px}
.stat{top:611px;width:252px;height:123px;background:rgba(70,88,130,.75);border-radius:8px;display:flex;align-items:center;padding-left:22px;gap:14px}
.stat b{font-size:32px;font-weight:700;color:var(--accent)}
.stat span{font-size:11px;line-height:19px;font-weight:500}

/* about */
.eyebrow{font-size:14px;font-weight:500}
.h2{font-size:28px;font-weight:700}
.about-copy{left:101px;top:966px;width:525px;font-size:12.5px;line-height:24.3px;color:var(--muted)}
.about-copy p+p{margin-top:5px}
.photo{border-radius:12px}
.glow{border-radius:50%;background:radial-gradient(circle,rgba(27,166,228,.28) 0,rgba(27,166,228,0) 70%)}

.intro-copy{top:1606px;left:180px;width:840px;text-align:center;font-size:12.5px;line-height:24.5px;color:var(--muted)}
.case{top:1761px;width:327px;height:146px;border-radius:8px;padding:36px 27px}
.case b{display:block;font-size:32px;font-weight:700}
.case span{display:block;margin-top:8px;font-size:13px;font-weight:700}

.quote{top:2192px;width:273px;height:278px;background:rgba(58,75,115,.75);border-radius:6px;padding:34px 24px 0 24px}
.quote p{font-size:12.3px;line-height:24.4px;color:var(--muted)}
.who{position:absolute;left:24px;bottom:20px;display:flex;align-items:center;gap:10px}
.avatar{width:30px;height:30px;border-radius:50%;background:#c9a99a}
.who b{display:block;font-size:12px;font-weight:700}
.who small{font-size:11px;color:var(--muted)}
.arrow-c{width:28px;height:28px;border-radius:50%;background:#d7dceb;display:flex;align-items:center;justify-content:center}

.faq{left:280px;width:614px;border:1px solid var(--line);border-radius:4px;padding:0 20px;font-size:13.5px;font-weight:500;display:flex;align-items:center;justify-content:space-between;color:var(--muted)}
.faq-open{top:2833px;height:131px;display:block;padding-top:17px;color:var(--white)}
.faq-open p{margin-top:8px;font-size:12.5px;line-height:24px;color:var(--muted);font-weight:400}

.blog{top:3460px;height:306px;border-radius:8px;padding:26px}
.blog h4{font-size:14px;font-weight:700;line-height:22px}
.blog p{font-size:10.5px;line-height:18px;color:#e1e6f0}
.blog-go{position:absolute;right:26px;bottom:22px;width:26px;height:26px;border-radius:50%;background:#2a2f3a}

.cta{left:136px;top:3900px;width:928px;height:283px;background:var(--panel);border-radius:10px}

.f-col{font-size:13px;line-height:26px;color:var(--muted)}
.f-head{font-size:13px;font-weight:700;color:var(--white)}
.input{left:821px;width:224px;height:35px;border:1px solid var(--line);border-radius:4px;font-size:11px;color:var(--muted);padding:10px 14px}
.legal{top:4472px;font-size:11px;color:var(--muted)}
</style>
</head>
<body>

<!-- Hero -->
<div class="abs hero-photo" role="img" aria-label="Photo of a smiling team of doctors and nurses in white coats"></div>
<div class="abs brand"><span class="brand-dot"></span>halcyon</div>
<div class="abs brand-sub">CONSULTING</div>
<nav class="abs nav"><span>Home</span><span>About</span><span>Portfolio</span><span>Our Services</span><span>Blog</span></nav>
<div class="abs follow">Follow Us <span class="soc"></span><span class="soc"></span></div>
<div class="btn btn-primary" style="left:994px;top:30px;width:101px;height:31px">Contact Us</div>

<div class="abs center hero-kicker">Don't miss a new opportunity to grow you practice with your<br>online presence.</div>
<h1 class="abs center hero-title">Being <span class="accent">online:</span><br>A Large Opportunity For Your <span class="accent">Practice.</span></h1>
<div class="btn btn-light" style="left:520px;top:487px;width:158px;height:39px">Start Your Project</div>

<div class="abs stat" style="left:75px"><b>80%</b><span>of internet uses search<br>for health information</span></div>
<div class="abs stat" style="left:341px"><b>50%</b><span>would like information<br>about a specific<br>health professional</span></div>
<div class="abs stat" style="left:606px"><b>42%</b><span>of individuals look at<br>health related<br>consumer reviews</span></div>
<div class="abs stat" style="left:872px"><b>41%</b><span>of consumers say<br>online presence may<br>impact their choice of<br>health professional</span></div>

<!-- About -->
<div class="abs glow" style="left:880px;top:950px;width:420px;height:420px"></div>
<div class="abs eyebrow" style="left:101px;top:886px">Halcyon Consulting</div>
<h2 class="abs h2" style="left:101px;top:912px">Helping Those Who Help <span class="accent">Others</span></h2>
<div class="abs about-copy">
  <p>You became a health professional because you wanted to make a difference and you obviously care about patient outcomes. At first things were great and you had plenty of patients but in the last few years there's more competition offering the same types of services and products that you do. Regular customers haven't come back to you in a while and you know you NEED to do something but the old ways like relying on word of mouth doesn't seem to be working well anymore and you don't know how to get started. But that's where we can help... Halcyon Consulting specialises in helping health professionals like you to create a great online user experience for your patients</p>
  <p>We help you build your online assets through Website development, social media marketing, Online Traffic Strategies.</p>
</div>
<div class="btn btn-primary" style="left:101px;top:1265px;width:124px;height:40px">Contact Us</div>
<div class="btn btn-light" style="left:255px;top:1265px;width:156px;height:40px">Start Your Project</div>
<div class="abs photo" style="left:657px;top:943px;width:468px;height:323px;background:linear-gradient(135deg,#b9c6d6,#8aa2bd 55%,#c39a85)" role="img" aria-label="Photo of a doctor using a tablet with a glowing digital health overlay"></div>

<!-- Intro -->
<div class="abs glow" style="left:880px;top:1650px;width:360px;height:360px"></div>
<div class="abs center eyebrow" style="top:1527px">Helping clients since 2015:</div>
<h2 class="abs center h2" style="top:1553px">Halcyon <span class="accent">Consulting</span></h2>
<div class="abs intro-copy">specialises in helping health professionals &nbsp;like you, stand out from the busy crowd, find new patient and helps<br>you be seen as the go-to person within your industry. Unlike most health professionals who solely rely on word of mouth, we<br>use the latest online marketing techniques to grow you and your practice.<br>While our niche has always been in the healthcare industry, Halcyon Marketing also has experience in providing solutions<br>our e-commerce partners as well as other professional industries.</div>
<div class="abs case" style="left:94px;background:linear-gradient(120deg,#2f5a8c,#6f9cc4)" role="img" aria-label="Image of a stethoscope with digital health icons"><b>63%</b><span>Healthcare and medical</span></div>
<div class="abs case" style="left:437px;background:linear-gradient(120deg,#3e6a95,#b9a58a)" role="img" aria-label="Image of hands reviewing printed sales charts"><b>25%</b><span>Ecommerce projects</span></div>
<div class="abs case" style="left:779px;background:linear-gradient(120deg,#4f74a3,#d8dee8)" role="img" aria-label="Image of professional service line icons"><b>12%</b><span>Other professional services</span></div>
<div class="btn btn-primary" style="left:445px;top:1953px;width:123px;height:38px">Contact Us</div>
<div class="btn btn-light" style="left:597px;top:1953px;width:158px;height:38px">Start Your Project</div>

<!-- Testimonials -->
<div class="abs center eyebrow" style="top:2086px">Testimonials</div>
<h2 class="abs center h2" style="top:2112px">See What Our Clients <span class="accent">Say</span></h2>
<div class="abs arrow-c" style="left:103px;top:2316px"><svg width="10" height="10" viewBox="0 0 10 10"><path d="M6.5 1.5 3 5l3.5 3.5" stroke="#1f3157" stroke-width="2" fill="none"/></svg></div>
<div class="abs arrow-c" style="left:1067px;top:2316px"><svg width="10" height="10" viewBox="0 0 10 10"><path d="M3.5 1.5 7 5 3.5 8.5" stroke="#1f3157" stroke-width="2" fill="none"/></svg></div>
<div class="abs quote" style="left:171px"><p>"Lorem ipsum dolor sit amet, consectetur adipiscing elit, sed do eiusmod tempor incididunt ut labore et dolore magna aliqua. Ut enim ad minim veniam, quis nostrud exercitation ullamco laboris nisi ut aliquip ex ea commodo consequat."</p><div class="who"><span class="avatar" role="img" aria-label="Client portrait"></span><div><b>Mara Velt</b><small>Creative Founder</small></div></div></div>
<div class="abs quote" style="left:465px"><p>"Lorem ipsum dolor sit amet, consectetur adipiscing elit, sed do eiusmod tempor incididunt ut labore et dolore magna aliqua. Ut enim ad minim veniam, quis nostrud exercitation ullamco laboris nisi ut aliquip ex ea commodo consequat."</p><div class="who"><span class="avatar" role="img" aria-label="Client portrait"></span><div><b>Lena Osric</b><small>Managing Director</small></div></div></div>
<div class="abs quote" style="left:758px"><p>"Lorem ipsum dolor sit amet, consectetur adipiscing elit, sed do eiusmod tempor incididunt ut labore et dolore magna aliqua. Ut enim ad minim veniam, quis nostrud exercitation ullamco laboris nisi ut aliquip ex ea commodo consequat."</p><div class="who"><span class="avatar" role="img" aria-label="Client portrait"></span><div><b>Tom Ardell</b><small>Sales Operator</small></div></div></div>
<div class="btn btn-primary" style="left:445px;top:2521px;width:123px;height:38px">Contact Us</div>
<div class="btn btn-light" style="left:597px;top:2521px;width:158px;height:38px">Start Your Project</div>

<!-- FAQ -->
<div class="abs center eyebrow" style="top:2738px">Have A Question?</div>
<h2 class="abs center h2" style="top:2760px">Frequently Asked <span class="accent">Questions</span></h2>
<div class="abs faq faq-open">Lorem ipsum dolor sit amet, consectetur adipiscing elit?
  <svg class="abs" style="right:18px;top:20px" width="10" height="8" viewBox="0 0 10 8"><path d="M1 2l4 4 4-4" stroke="#fff" stroke-width="1.5" fill="none"/></svg>
  <p>Lorem ipsum dolor amet consec tetur adipiscing elit eiusmod tempor incididunt<br>labore dolore magna alirua enim minim veniam nostrud exerci tation ullamco<br>laboris.</p></div>
<div class="abs faq" style="top:2980px;height:56px">Ipsum dolor sit amet, consectetur adipiscing elit?<span>›</span></div>
<div class="abs faq" style="top:3050px;height:56px">Sed do eiusmod tempor incididunt ut labore et dolore magna aliqua?<span>›</span></div>
<div class="abs faq" style="top:3121px;height:56px">Ut enim ad minim veniam, quis nostrud exercitation ullamco laboris?<span>›</span></div>

<!-- Blog -->
<div class="abs center eyebrow" style="top:3380px">Halcyon Consulting</div>
<h2 class="abs center h2" style="top:3403px">Our Latest <span class="accent">Blogs</span></h2>
<div class="abs blog" style="left:143px;width:446px;padding-top:124px;background:linear-gradient(120deg,#7c8fb0,#cdb7c4)" role="img" aria-label="Photo of a hand holding a phone with social media icons">
  <h4>Lorem ipsum dolor sit amet,<br>consectetur adipiscing elit.</h4>
  <p style="margin-top:10px">Lorem ipsum dolor amet consec tetur adipiscing elit eiusmod tempor incididunt labore dolore magna alirua enim minim veniam nostrud exerci tation ullamco laboris.</p>
  <p style="margin-top:6px">Consec tetur adipiscing elit eiusmod tempor incididunt labore dolore magna laboris.</p></div>
<div class="abs blog" style="left:618px;width:205px;background:linear-gradient(160deg,#6d5a52,#2d2a30)" role="img" aria-label="Photo of a business handshake"><h4>Lorem ipsum dolor<br>sit amet,consectetur.</h4><span class="blog-go"></span></div>
<div class="abs blog" style="left:852px;width:205px;background:linear-gradient(160deg,#a9b9c8,#d6aaa6)" role="img" aria-label="Photo of a doctor holding a piggy bank"><h4>Lorem ipsum dolor<br>sit amet.</h4><span class="blog-go"></span></div>
<div class="btn btn-light" style="left:545px;top:3804px;width:108px;height:39px">View All</div>

<!-- CTA -->
<div class="abs cta"></div>
<div class="abs center eyebrow" style="top:3959px">Get In Touch</div>
<h2 class="abs center h2" style="top:3988px;font-size:32px">Halcyon <span class="accent">Consulting</span></h2>
<div class="abs center" style="top:4037px;font-size:15px;font-weight:500">Being online: a large opportunity for your practice.</div>
<div class="btn btn-primary" style="left:520px;top:4087px;width:158px;height:39px">Start Your Project</div>

<!-- Footer -->
<div class="abs brand" style="top:4240px;color:#d5dbe8"><span class="brand-dot"></span>halcyon</div>
<div class="abs brand-sub" style="top:4274px">CONSULTING</div>
<div class="abs f-head" style="left:351px;top:4246px">Links</div>
<div class="abs f-col" style="left:351px;top:4277px">Home<br>About<br>Portfolio<br>Contact Us<br>Our Services<br>Blog</div>
<div class="abs f-head" style="left:552px;top:4246px">Contact</div>
<div class="abs f-col" style="left:552px;top:4277px">info@halcyonconsulting.example</div>
<div class="abs f-head" style="left:552px;top:4334px;font-size:11px">Follow Us</div>
<div class="abs follow" style="left:552px;top:4357px"><span class="soc"></span><span class="soc"></span></div>
<div class="abs f-head" style="left:821px;top:4246px">Sign up</div>
<div class="abs f-col" style="left:821px;top:4277px">to our mailing list</div>
<div class="abs input" style="top:4313px">Name</div>
<div class="abs input" style="top:4357px">Email</div>
<div class="btn btn-light" style="left:821px;top:4400px;width:105px;height:33px">Subscribe</div>
<div class="abs legal" style="left:110px">Privacy Policy</div>
<div class="abs legal center">Copyright 2022 © Halcyonconsulting.</div>
<div class="abs legal" style="left:970px;width:118px;text-align:right">Terms and conditions</div>

</body>
</html>
```